Rehearsal studio business card design needed

My rehearsal studio i bought not that long ago was opened as a hobby originally and was definitely not taken seriously. I am trying to make the new look studio be launched with the new look business cards. I am looking for very simple and clean look cards to match the simple and clean studios. the colour scheme is red and grey. over all i am really just looking for a very simple card that is not too busy and just gets the point accross.
Target Market(s)
Targeting bands, music teachers, students, etc.
Industry/Entity Type
Business
Contact Information for Business Card
Bellwater Sound Centre
Rehearsal and Recording Facilities
Owen Taft CEO
unit 8, 47 Marlow Street Penfield NSW 2093
0438 915 264
bellwatersoundcentre@quillmail.example
Requirements
Must have
- simplicity
Nice to have
- black background using the 'white.png' file

```html
<!DOCTYPE html>
<html lang="en">
<head>
<meta charset="utf-8">
<title>Bellwater Sound Centre – Business Cards</title>
<link rel="stylesheet" href="https://fonts.googleapis.com/css2?family=Poiret+One&display=swap">
<style>
  :root {
    --page: #f2f2f2;
    --ink: #ffffff;
    --card-black: #1d1c1e;
    --red-light: #c91c2e;
    --red-dark: #7c0e18;
    --bar-light: #a2a2a2;
    --bar-dark: #4a4a4a;
    --silver-light: #e6e6e6;
    --silver-dark: #6e6e6e;
    --card-shadow: rgba(0, 0, 0, 0.35);
  }
  * { box-sizing: border-box; margin: 0; padding: 0; }
  html, body {
    width: 1200px;
    height: 800px;
    overflow: hidden;
    background: var(--page);
  }
  .canvas {
    position: relative;
    width: 1200px;
    height: 800px;
    font-family: "Poiret One", sans-serif;
    color: var(--ink);
  }
  .card {
    position: absolute;
    width: 540px;
    height: 300px;
    box-shadow: 0 10px 24px var(--card-shadow);
    overflow: hidden;
  }
  .card svg.card-art {
    position: absolute;
    inset: 0;
    width: 100%;
    height: 100%;
    z-index: 0;
  }
  .card-back { left: 50px; top: 70px; }
  .card-front { left: 610px; top: 430px; }

  .contact {
    position: absolute;
    inset: 0;
    z-index: 1;
    text-align: center;
    white-space: nowrap;
    text-shadow: 1px 2px 2px rgba(0, 0, 0, 0.85), 0 0 3px rgba(0, 0, 0, 0.6);
  }
  .contact .company {
    position: absolute;
    top: 48px;
    width: 100%;
    font-size: 27px;
    letter-spacing: 0.5px;
  }
  .contact .tagline {
    position: absolute;
    top: 82px;
    width: 100%;
    font-size: 14px;
    font-variant: small-caps;
    letter-spacing: 0.8px;
  }
  .contact .person {
    position: absolute;
    top: 138px;
    width: 100%;
    font-size: 15px;
    line-height: 1.35;
  }
  .contact .phone {
    position: absolute;
    top: 196px;
    width: 100%;
    font-size: 20px;
  }
  .contact .email {
    position: absolute;
    top: 250px;
    width: 100%;
    font-size: 18.5px;
    letter-spacing: 0.2px;
  }

  .brand-badge {
    position: absolute;
    z-index: 1;
    left: 300px;
    top: 34px;
    width: 190px;
    text-align: center;
  }
  .brand-badge .badge-name {
    margin-top: 10px;
    font-size: 17px;
    letter-spacing: 1px;
    white-space: nowrap;
  }
  .brand-wordmark {
    position: absolute;
    z-index: 1;
    left: 225px;
    top: 222px;
    width: 300px;
    text-align: center;
    font-size: 25px;
    letter-spacing: 0.5px;
    white-space: nowrap;
  }
</style>
</head>
<body>
<main class="canvas">

  <section class="card card-back" aria-label="Business card, contact side">
    <svg class="card-art" viewBox="0 0 540 300" aria-hidden="true">
      <defs>
        <linearGradient id="red-fade" x1="0" y1="0" x2="0" y2="1">
          <stop offset="0" stop-color="var(--red-light)"/>
          <stop offset="1" stop-color="var(--red-dark)"/>
        </linearGradient>
        <linearGradient id="bar-fade" x1="0" y1="0" x2="1" y2="0">
          <stop offset="0" stop-color="var(--bar-dark)"/>
          <stop offset="0.5" stop-color="var(--bar-light)"/>
          <stop offset="1" stop-color="var(--bar-dark)"/>
        </linearGradient>
      </defs>
      <rect class="back-field" width="540" height="300" fill="url(#red-fade)"/>
      <ellipse class="back-disc" cx="270" cy="150" rx="255" ry="200" fill="var(--card-black)"/>
      <rect class="centre-band" x="188" y="0" width="142" height="300" fill="url(#red-fade)"/>
      <rect class="band-edge" x="172" y="0" width="16" height="300" fill="url(#bar-fade)"/>
      <rect class="band-edge" x="330" y="0" width="16" height="300" fill="url(#bar-fade)"/>
    </svg>
    <div class="contact">
      <p class="company">Bellwater Sound Centre</p>
      <p class="tagline">Rehearsal and Recording Facilities</p>
      <p class="person">Owen Taft CEO unit 8<br>47 Marlow Street Penfield NSW 2093</p>
      <p class="phone">0438 915 264</p>
      <p class="email">bellwatersoundcentre@quillmail.example</p>
    </div>
  </section>

  <section class="card card-front" aria-label="Business card, brand side">
    <svg class="card-art" viewBox="0 0 540 300" aria-hidden="true">
      <defs>
        <linearGradient id="red-fade-front" x1="0" y1="0" x2="0" y2="1">
          <stop offset="0" stop-color="var(--red-light)"/>
          <stop offset="1" stop-color="var(--red-dark)"/>
        </linearGradient>
        <linearGradient id="silver-fade-front" x1="0" y1="0" x2="1" y2="0">
          <stop offset="0" stop-color="var(--silver-light)"/>
          <stop offset="1" stop-color="var(--silver-dark)"/>
        </linearGradient>
      </defs>
      <rect class="front-field" width="540" height="300" fill="var(--card-black)"/>
      <polygon class="red-sweep" points="0,0 148,0 308,300 0,300" fill="url(#red-fade-front)"/>
      <polygon class="silver-sweep" points="148,0 166,0 330,300 308,300" fill="url(#silver-fade-front)"/>
    </svg>
    <div class="brand-badge">
      <svg width="80" height="80" viewBox="0 0 80 80" aria-hidden="true">
        <circle cx="40" cy="40" r="38" fill="var(--red-light)"/>
      </svg>
      <p class="badge-name">bellwater sound centre</p>
    </div>
    <p class="brand-wordmark">bellwater sound centre</p>
  </section>

</main>
</body>
</html>
```